Handelsunternehmen für haltbare Lebensmittel benötigt Webdesign
Zielgruppe
Wir sind ein Hamburger Handelsunternehmen für haltbare Lebensmittel.
Durch diese Website soll ein Interesse geweckt werden zur Zusammenarbeit und womöglich zur Kooperation der verschiedensten Großhändler des Food-Sektors mit der Vornalto GmbH. Endverbraucher können sich aufgrund der Entdeckung unseres Firmennamens informieren wer wir sind und was wir machen.
Aufgabenstellung
Bitte unterstützt uns bei der Erstellung einer Website unserer Unternehmen. Diese Website soll für unsere Firma Vornalto GmbH sein. Bitte deshalb auch nur den Fokus auf Design für die vornalto.de Seite legen.
Ein externer Shop unter dem Namen kelmstrand.de der Produkte der Kelmstrand vertreibt soll zu einem späteren Zeitpunkt folgen. Dieser Link sollte zwingend im Design als link involviert sein.
Dem Anhang beigefügt findet Ihr unsere beiden Logos.
Da sich unsere zweite Marke Kelmstrand in Zukunft durch das Thema Hamburg optisch definieren soll, beachtet bitte das Vornalto themenübergreifend und generisch funktioniert.
Neu**********Um einen stimmungsvollen Gesamteindruck zu erzeugen im Banner, bitten wir um Verwendung moderner, natürlicher Bilder aus den Bereichen Frische und Natur. Durch florale Illustrationen sollen Akzente gesetzt werden und der Look aufgelockert sein.*************Neu
Unsere Zielgruppe sind erfahrene oder nichterfahrene kochbegeisterte Entdecker kulinarischer Genüsse die sich aufgrund der Entdeckung des Firmennamens auf unseren Artikeln des Kelmstrand Portfolios über die Herkunft des Unternehmens informieren möchten. Die Zielgruppe zeichnet sich durch Spontanität und Individualität aus. Werbung gegenüber ist die Zielgruppe sehr aufgeschlossen. Beim Einkauf ist ihnen Qualität wichtiger als der Preis. Sie konsumieren gerne Markenartikel und bevorzugen beim Einkauf eine Inspiration die wir Ihnen über die Website mitgeben werden. Die Umweltverträglichkeit von Produkten spielt für sie eine große Rolle. Nachhaltigkeit ist ihnen wichtig.
Wir wünschen uns einen hohen Wiedererkennungswert der durch unseren internationalen Namen begründet ist und einer europaweiten Expansion nichts im Wege steht.
Es soll ein OnePager werden der auch in der Mobilversion gut funktionieren muss. Also muss die Responsivität sehr gut umgesetzt sein.
Der Firmenauftritt soll grob wie folgt aufgebaut sein:
Home
LOGO(De..

```html
<!DOCTYPE html>
<html lang="de">
<head>
<meta charset="utf-8">
<title>Vornalto – Gewürze</title>
<link rel="stylesheet" href="https://fonts.googleapis.com/css2?family=Montserrat:ital,wght@0,400;0,500;0,600;0,700;0,800;1,500&family=Great+Vibes&display=swap">
<style>
:root{
  --accent:#f4b825;
  --ink:#121212;
  --muted:#5a5f66;
  --pale:#cad8e3;
  --field:#eef2f6;
  --footer:#2c2f3d;
  --line:#cfe0ea;
  --white:#ffffff;
  --thumb-ring:#e3ebf1;
}
*{box-sizing:border-box;margin:0;padding:0}
html,body{width:1200px;height:3102px;overflow:hidden}
body{font-family:'Montserrat',sans-serif;color:var(--ink);background:var(--white);position:relative}
.abs{position:absolute}

/* hero */
.hero{left:0;top:0;width:1200px;height:675px;
  background:radial-gradient(circle at 30% 20%,#c9742a 0,transparent 35%),radial-gradient(circle at 75% 25%,#a98f2c 0,transparent 35%),radial-gradient(circle at 80% 75%,#7d2a1c 0,transparent 35%),radial-gradient(circle at 20% 75%,#5b3420 0,transparent 40%),linear-gradient(160deg,#4a3424,#2a2019 60%,#3c2a1e)}
.topbar{left:0;top:0;width:1200px;height:48px;background:rgba(20,20,20,.6)}
.contact-item{top:18px;font-size:11px;line-height:13px;color:var(--white);display:flex;align-items:center;gap:8px;white-space:nowrap}
.search{left:870px;top:10px;width:218px;height:28px;background:rgba(20,20,20,.8);border-radius:2px;font-size:11px;font-style:italic;color:#ddd;padding:7px 16px}
.search svg{position:absolute;right:10px;top:6px}
.logo{font-weight:800;letter-spacing:2px;color:#fff;display:flex;align-items:center;gap:8px}
.logo .dot{width:10px;height:10px;border-radius:50%;background:var(--accent)}
.nav{top:70px;font-size:13px;font-weight:500;color:#fff}
.script{left:0;width:1200px;top:140px;text-align:center;font-family:'Great Vibes',cursive;font-size:190px;color:var(--accent);line-height:1}
.tagline{left:581px;top:364px;font-size:20px;font-style:italic;font-weight:500;color:#fff}
.arrow{top:290px}

/* welcome */
.welcome{left:111px;top:507px;width:978px;height:376px;background:var(--pale)}
.welcome h1{position:absolute;left:49px;top:46px;font-size:36px;font-weight:700}
.welcome h2{position:absolute;left:49px;top:101px;width:400px;font-size:18px;font-weight:700;line-height:25px}
.welcome p{position:absolute;left:49px;top:182px;width:482px;font-size:14px;line-height:20.5px}
.welcome .photo{position:absolute;right:0;top:0;width:343px;height:376px;
  background:radial-gradient(circle at 50% 55%,#9a4524 0,#6e5a4c 40%,#a9b6c0 80%,#c4ced6 100%)}

.section-title{left:0;width:1200px;text-align:center;font-size:36px;font-weight:700}

/* product cards */
.card{top:1038px;width:224px;height:328px;border:1px solid #d7e4ec;background:#fff;text-align:center}
.card .thumb{width:149px;height:149px;border-radius:50%;margin:36px auto 0;border:3px solid var(--thumb-ring)}
.card h3{margin-top:18px;font-size:18px;font-weight:600}
.card p{margin:6px auto 0;width:160px;font-size:12.5px;line-height:17px;color:var(--muted)}
.btn{display:inline-block;margin-top:18px;width:128px;height:30px;border:1px solid var(--accent);border-radius:15px;color:var(--accent);font-size:12px;font-weight:600;line-height:28px}
.dots{left:0;width:1200px;top:1393px;display:flex;justify-content:center;gap:8px}
.dots span{width:9px;height:9px;border-radius:50%;background:#f7d27a}
.dots span.on{background:#fff;border:2px solid var(--accent)}

/* portfolio */
.pf{width:476px;height:155px;border-bottom:1px solid var(--line)}
.pf .thumb{position:absolute;left:0;top:8px;width:102px;height:102px;border-radius:50%;border:4px solid var(--thumb-ring)}
.pf h3{position:absolute;left:120px;top:0;font-size:18px;font-weight:600}
.pf p{position:absolute;left:120px;top:27px;width:360px;font-size:12.5px;line-height:20.5px;color:var(--muted)}

/* contact */
.contact{left:0;top:2240px;width:1200px;height:558px;background:var(--pale)}
.contact .left-photo{position:absolute;left:0;top:0;width:325px;height:558px;background:radial-gradient(circle at 30% 25%,#8f2a20 0,#5a3a28 30%,transparent 70%),linear-gradient(90deg,#6d5443,var(--pale))}
.contact .right-photo{position:absolute;left:858px;top:70px;width:342px;height:488px;background:radial-gradient(circle at 70% 40%,#9b2020 0,#b87a3a 40%,transparent 75%)}
.contact h2{position:absolute;left:0;width:1200px;top:72px;text-align:center;font-size:36px;font-weight:700}
.contact .sub{position:absolute;left:0;width:1200px;top:128px;text-align:center;font-size:14px}
.field{position:absolute;height:45px;background:var(--field);border-radius:4px;font-size:14px;color:#444;padding:13px 16px}
.submit{position:absolute;left:543px;top:430px;width:117px;height:42px;border-radius:21px;background:var(--accent);color:#fff;font-size:14px;font-weight:500;letter-spacing:1.5px;text-align:center;line-height:42px}

/* footer */
.footer{left:0;top:2798px;width:1200px;height:304px;background:var(--footer);color:#fff}
.footer .line{position:absolute;left:0;width:1200px;text-align:center;font-size:12px;color:#d9dbe2}
.socials{position:absolute;left:0;width:1200px;top:211px;display:flex;justify-content:center;gap:7px}
.socials span{width:27px;height:27px;border-radius:50%;background:#243b6e}
.socials span.up{background:#6b6f7c}
.socials span.hl{background:var(--accent)}
</style>
</head>
<body>

<div class="abs hero" role="img" aria-label="Foto: Schalen und Löffel mit bunten Gewürzen, Kräutern und Pfefferkörnern"></div>
<div class="abs topbar"></div>
<div class="abs contact-item" style="left:111px">
  <svg width="11" height="11" viewBox="0 0 24 24"><path d="M6 2l4 4-2 3c1 3 4 6 7 7l3-2 4 4-3 4C10 22 2 14 2 5z" fill="none" stroke="#fff" stroke-width="2"/></svg><span>040-555-0182</span>
</div>
<div class="abs contact-item" style="left:242px">
  <svg width="12" height="10" viewBox="0 0 24 18"><rect x="1" y="1" width="22" height="16" fill="none" stroke="#fff" stroke-width="2"/><path d="M1 1l11 9 11-9" fill="none" stroke="#fff" stroke-width="2"/></svg><span>info@vornalto.de</span>
</div>
<div class="abs search">Search . . .
  <svg width="15" height="15" viewBox="0 0 24 24"><circle cx="10" cy="10" r="7" fill="none" stroke="#fff" stroke-width="2"/><path d="M15 15l6 6" stroke="#fff" stroke-width="2"/></svg>
</div>
<div class="abs logo" style="left:111px;top:62px;font-size:30px">VORNALTO<span class="dot"></span></div>
<div class="abs nav" style="left:535px">Home</div>
<div class="abs nav" style="left:627px">|</div>
<div class="abs nav" style="left:686px">Portfolio</div>
<div class="abs nav" style="left:793px">|</div>
<div class="abs nav" style="left:851px">Online Shop</div>
<div class="abs nav" style="left:981px">|</div>
<div class="abs nav" style="left:1040px">Kontakt</div>
<div class="abs script">Spices</div>
<div class="abs tagline">Sed ut perspiciatis unde</div>
<svg class="abs arrow" style="left:110px" width="20" height="28" viewBox="0 0 20 28"><path d="M16 3L5 14l11 11" fill="none" stroke="#fff" stroke-width="4"/></svg>
<svg class="abs arrow" style="left:1070px" width="20" height="28" viewBox="0 0 20 28"><path d="M4 3l11 11L4 25" fill="none" stroke="#fff" stroke-width="4"/></svg>

<section class="abs welcome">
  <h1>Willkommen</h1>
  <h2>Mistaken idea of denouncing pleasure and praising pain was born and I will give you a complete</h2>
  <p>No one rejects, dislikes, or avoids pleasure itself, because it is pleasure, but because those who do not know how to pursue pleasure rationally encounter consequences that are extremely painful. Nor again is there anyone who loves or pursues or desires to obtain pain of itself, because it is pain, but because occasionally circumstances occur in which toil and pain can procure him some great pleasure. To take a trivial example.</p>
  <div class="photo" role="img" aria-label="Foto: Schälchen mit Gewürzen, Sternanis und Messlöffeln auf grauem Grund"></div>
</section>

<h2 class="abs section-title" style="top:960px">Products</h2>
<div class="abs card" style="left:112px"><div class="thumb" role="img" aria-label="Produktfoto: drei Gewürzbeutel in Schwarz, Weiß und Braun" style="background:linear-gradient(180deg,#e4ecf2 0,#e4ecf2 32%,#4a3a32 32%,#8a6a52 68%,#e4ecf2 68%)"></div><h3>Safran</h3><p>Et harum quidem rerum facilis est et expedita.</p><span class="btn">SHOP NOW</span></div>
<div class="abs card" style="left:362px"><div class="thumb" role="img" aria-label="Produktfoto: vier weiße Gewürzdosen" style="background:linear-gradient(180deg,#e4ecf2 0,#e4ecf2 28%,#f8f9fa 28%,#cfd6dc 72%,#e4ecf2 72%)"></div><h3>Gewürze und Kräuter</h3><p>Et harum quidem rerum facilis est et expedita.</p><span class="btn">SHOP NOW</span></div>
<div class="abs card" style="left:612px"><div class="thumb" role="img" aria-label="Produktfoto: weißer Stoffbeutel" style="background:radial-gradient(ellipse 30% 45% at 50% 55%,#ffffff 0,#f1f3f5 70%,#dfe8ee 100%)"></div><h3>Trockenfrüchte</h3><p>Et harum quidem rerum facilis est et expedita.</p><span class="btn">SHOP NOW</span></div>
<div class="abs card" style="left:862px"><div class="thumb" role="img" aria-label="Produktfoto: vier Metalldosen" style="background:linear-gradient(180deg,#e4ecf2 0,#e4ecf2 30%,#8e959c 30%,#5d646b 70%,#e4ecf2 70%)"></div><h3>Pistazien</h3><p>Et harum quidem rerum facilis est et expedita.</p><span class="btn">SHOP NOW</span></div>
<div class="abs dots"><span></span><span class="on"></span><span></span></div>

<h2 class="abs section-title" style="top:1481px">Portfolio</h2>
<div class="abs pf" style="left:111px;top:1559px"><div class="thumb" role="img" aria-label="Foto: Safranfäden" style="background:linear-gradient(135deg,#c42a1e,#7a1410)"></div><h3>Safran</h3><p>Nor again is there anyone who loves or pursues or desires to obtain pain of itself, because it is pain, but because occasionally circumstances occur in which toil and pain can procure him some great pleasure.</p></div>
<div class="abs pf" style="left:613px;top:1559px"><div class="thumb" role="img" aria-label="Foto: Gewürzsäckchen" style="background:linear-gradient(135deg,#f4efe8 0,#c98a3a 50%,#a8432a)"></div><h3>Gewürze und Kräuter</h3><p>Nor again is there anyone who loves or pursues or desires to obtain pain of itself, because it is pain, but because occasionally circumstances occur in which toil and pain can procure him some great pleasure.</p></div>
<div class="abs pf" style="left:111px;top:1714px"><div class="thumb" role="img" aria-label="Foto: getrocknete Früchte" style="background:linear-gradient(135deg,#d9b46a,#e0862a 50%,#4a2a3a)"></div><h3>Trockenfrüchte</h3><p>Nor again is there anyone who loves or pursues or desires to obtain pain of itself, because it is pain, but because occasionally circumstances occur in which toil and pain can procure him some great pleasure.</p></div>
<div class="abs pf" style="left:613px;top:1714px"><div class="thumb" role="img" aria-label="Foto: Pistazien" style="background:linear-gradient(160deg,#f6f4ef 0,#7a9a3a 40%,#c9a97a 75%,#f6f4ef)"></div><h3>Pistazien</h3><p>Nor again is there anyone who loves or pursues or desires to obtain pain of itself, because it is pain, but because occasionally circumstances occur in which toil and pain can procure him some great pleasure.</p></div>
<div class="abs pf" style="left:111px;top:1869px"><div class="thumb" role="img" aria-label="Foto: Teeblätter" style="background:linear-gradient(180deg,#f3f5f2 0,#4c8a2a 40%,#3a3028 75%)"></div><h3>Tee</h3><p>Nor again is there anyone who loves or pursues or desires to obtain pain of itself, because it is pain, but because occasionally circumstances occur in which toil and pain can procure him some great pleasure.</p></div>
<div class="abs pf" style="left:613px;top:1869px"><div class="thumb" role="img" aria-label="Foto: Sonnenblume und Öl" style="background:linear-gradient(135deg,#ffffff 0,#f2c21a 45%,#d89a10 80%,#3a3a3a)"></div><h3>Öl</h3><p>Nor again is there anyone who loves or pursues or desires to obtain pain of itself, because it is pain, but because occasionally circumstances occur in which toil and pain can procure him some great pleasure.</p></div>
<div class="abs pf" style="left:111px;top:2024px"><div class="thumb" role="img" aria-label="Foto: Reiskörner" style="background:linear-gradient(135deg,#ffffff,#e2e2e0)"></div><h3>Reis</h3><p>Nor again is there anyone who loves or pursues or desires to obtain pain of itself, because it is pain, but because occasionally circumstances occur in which toil and pain can procure him some great pleasure.</p></div>

<section class="abs contact">
  <div class="left-photo" role="img" aria-label="Foto: Nelken, Pfefferkörner und Chili"></div>
  <div class="right-photo" role="img" aria-label="Foto: Schalen mit Gewürzen, Chilischoten und Sternanis"></div>
  <h2>Kontakt</h2>
  <div class="sub">Lorem Ipsum is simply dummy text of the printing and typesetting</div>
  <div class="field" style="left:359px;top:172px;width:233px">Name:</div>
  <div class="field" style="left:610px;top:172px;width:234px">Email:</div>
  <div class="field" style="left:359px;top:235px;width:233px">Phone:</div>
  <div class="field" style="left:610px;top:235px;width:234px">Company:</div>
  <div class="field" style="left:359px;top:298px;width:485px;height:114px">Message:</div>
  <div class="submit">SUBMIT</div>
</section>

<footer class="abs footer">
  <div class="logo" style="position:absolute;left:0;width:1200px;justify-content:center;top:78px;font-size:40px">VORNALTO<span class="dot"></span></div>
  <div class="line" style="top:140px">
    <svg width="9" height="12" viewBox="0 0 18 24" style="vertical-align:-1px;margin-right:4px"><path d="M9 0a9 9 0 00-9 9c0 7 9 15 9 15s9-8 9-15a9 9 0 00-9-9z" fill="#f4b825"/><circle cx="9" cy="9" r="3" fill="#2c2f3d"/></svg>8 Kaimauerweg, 20457 Hamburg, Deutschland
  </div>
  <div class="line" style="top:168px">
    <span style="margin-right:34px"><svg width="11" height="8" viewBox="0 0 24 18" style="margin-right:8px"><rect x="1" y="1" width="22" height="16" fill="none" stroke="#f4b825" stroke-width="2"/><path d="M1 1l11 9 11-9" fill="none" stroke="#f4b825" stroke-width="2"/></svg>info@vornalto.de</span>
    <span style="margin-right:34px"><svg width="11" height="11" viewBox="0 0 24 24" style="margin-right:4px"><path d="M6 2l4 4-2 3c1 3 4 6 7 7l3-2 4 4-3 4C10 22 2 14 2 5z" fill="#f4b825"/></svg>040-555-0182</span>
    <span><svg width="12" height="10" viewBox="0 0 24 20" style="margin-right:6px"><rect x="2" y="6" width="20" height="12" fill="#f4b825"/><rect x="6" y="1" width="12" height="6" fill="none" stroke="#f4b825" stroke-width="2"/></svg>040-555-0183</span>
  </div>
  <div class="socials">
    <span class="up"></span><span></span><span></span><span></span><span class="hl"></span><span></span><span></span>
  </div>
</footer>

</body>
</html>
```